Broschüren-Design für Produzent von hochwertigen Verpackungs- und Präsentationslösungen
Zielgruppe
Wir produzieren hochwertige Verpackungs- und Präsentationslösungen.
Unsere Zielgruppe sind Firmen, welche kreative Premium-Packaging benötigt.
Aufgabenstellung
- Format: A4 hoch
- Umfang: 6 Seiten
- Falzart: Wickelfalz
- Design muss sehr hochwertig sein. Passend zu unseren Produktion (siehe Bilder)
- Wir möchten mit diesem Falzprospekt eine Übersicht über unsere Produkte generieren.
- Die Produkte sind bereits schon hochwertig fotografiert und müssen in einem anspruchsvollen Design in Szene gesetzt werden.
- Der Prospekt sollte die Kunden emotional berühren.
- Auf der Titelseite werden wir den Titel «High Performance Packaging» mit Folien prägen
- Seitenaufbau gemäss meiner Visualisierung (im Anhang)
- Bei jeder Produktkategorie möchte ich ein Grosses Übersichtsbild zusammen mit einem kurzen Text.
Ergänzend können noch weitere (passende) Bilder der jeweiligen Kategorie abgebildet werden.
Im Anhang finden Sie:
- Visualisierung des zu gestaltenden Prospekt
- Werbeflyer (zur Ansicht/Inspiration). In etwa so stellen wir uns das Design/Tonalität vor.
- Weitere passende Produktbilder können vorerst auf der Webseite unseres Produktionspartner (www.bogenhaus-muster.de) entnommen werden.

```html
<!DOCTYPE html>
<html lang="de">
<head>
<meta charset="utf-8">
<title>High Performance Packaging – Broschüre</title>
<link href="https://fonts.googleapis.com/css2?family=Poppins:wght@300;400;600;700&display=swap" rel="stylesheet">
<style>
:root{
  --bg:#d9d9db;
  --paper:#ffffff;
  --ink:#2c3142;
  --navy:#3f4660;
  --slate:#5e6579;
  --slate-light:#7d8394;
  --text:#6b6f7a;
  --photo-dark:#3a3b3f;
  --photo-mid:#57595e;
  --photo-brown:#7b5a4a;
}
*{box-sizing:border-box;margin:0;padding:0}
html,body{width:1200px;height:873px;overflow:hidden}
body{background:var(--bg);font-family:"Poppins",sans-serif;color:var(--ink);position:relative}
.page{position:absolute;top:176px;width:360px;height:520px;background:var(--paper);overflow:hidden}
.cover{left:24px;box-shadow:0 6px 18px rgba(0,0,0,.12)}
.spread-left{left:420px;box-shadow:-6px 6px 18px rgba(0,0,0,.12)}
.spread-right{left:780px;box-shadow:6px 6px 18px rgba(0,0,0,.12)}
.gutter{position:absolute;top:176px;left:776px;width:8px;height:520px;background:linear-gradient(90deg,rgba(0,0,0,0),rgba(0,0,0,.08),rgba(0,0,0,0));z-index:2}
.accent{position:absolute;height:8px;background:var(--navy)}
.accent.tr{top:0;right:0;width:100px;clip-path:polygon(0 0,100% 0,100% 100%,8px 100%)}
.accent.bl{bottom:0;left:0;width:100px;clip-path:polygon(0 0,calc(100% - 8px) 0,100% 100%,0 100%)}
.accent.br{bottom:0;right:0;width:100px;clip-path:polygon(8px 0,100% 0,100% 100%,0 100%)}
/* cover */
.cover-band{position:absolute;left:0;top:0;width:360px;height:520px}
.cover-photo{position:absolute;left:178px;top:110px;width:162px;height:175px;background:linear-gradient(135deg,var(--photo-brown),#5c4438 60%,var(--photo-dark))}
.cover-title{position:absolute;left:14px;top:168px;width:150px;text-align:right;font-weight:700;font-size:19px;line-height:1.12;color:var(--ink)}
.cover-sub{position:absolute;left:24px;top:300px;font-weight:300;font-size:13px;line-height:1.25;color:#fff}
/* inside */
.item{position:absolute}
.item h2{font-weight:700;font-size:12px;color:var(--ink);margin-bottom:4px}
.item p{font-weight:400;font-size:7px;line-height:1.6;color:var(--text)}
.product-photo{position:absolute;background:linear-gradient(135deg,var(--photo-mid),var(--photo-dark))}
</style>
</head>
<body>

<section class="page cover">
  <span class="accent tr"></span>
  <svg class="cover-band" viewBox="0 0 360 520" aria-hidden="true">
    <polygon points="0,240 150,240 165,225 360,225 360,300 260,300 245,315 245,345 0,345" fill="var(--slate-light)"/>
    <polygon points="0,250 360,250 360,295 255,295 240,310 240,370 0,370" fill="var(--slate)"/>
  </svg>
  <div class="cover-photo" role="img" aria-label="Produktfoto: braune Präsentationsmappe mit Musterkarten"></div>
  <h1 class="cover-title">High Performance Packaging</h1>
  <p class="cover-sub">Exklusive Verpackungsund<br>Präsentationslösungen</p>
  <span class="accent bl"></span>
</section>

<section class="page spread-left">
  <span class="accent tr"></span>
  <div class="product-photo" style="left:228px;top:62px;width:105px;height:85px" role="img" aria-label="Produktfoto: Verpackungsbox mit Einlage"></div>
  <div class="item" style="left:32px;top:85px;width:180px">
    <h2>Verpackungen</h2>
    <p>Lorem ipsum dolor sit amet, consetetur sadipscing elitr, sed diam nonumy eirmod tempor invidunt ut labore et dolore magna aliquyam erat, sed diam voluptua. At vero eos et accusam et justo duo dolores et ea rebum. Stet clita kasd gubergren, no sea</p>
  </div>
  <div class="product-photo" style="left:32px;top:192px;width:120px;height:90px" role="img" aria-label="Produktfoto: Präsentationsmappe mit Farbmustern"></div>
  <div class="item" style="left:168px;top:192px;width:165px">
    <h2>Präsentationsmappen</h2>
    <p>Lorem ipsum dolor sit amet, consetetur sadipscing elitr, sed diam nonumy eirmod tempor invidunt ut labore et dolore magna aliquyam erat, sed diam voluptua. At vero eos et accusam et justo duo dolores</p>
  </div>
  <div class="product-photo" style="left:200px;top:305px;width:133px;height:100px" role="img" aria-label="Produktfoto: Mustermappe aufgeklappt"></div>
  <div class="item" style="left:32px;top:415px;width:200px">
    <h2>Mustermappen</h2>
    <p>Lorem ipsum dolor sit amet, consetetur sadipscing elitr, sed diam nonumy eirmod tempor invidunt ut labore et dolore magna aliquyam erat, sed diam voluptua. At vero eos</p>
  </div>
  <span class="accent bl"></span>
</section>

<div class="gutter"></div>

<section class="page spread-right">
  <span class="accent tr"></span>
  <div class="item" style="left:28px;top:68px;width:182px">
    <h2>Ringordner</h2>
    <p>Lorem ipsum dolor sit amet, consetetur sadipscing elitr, sed diam nonumy eirmod tempor invidunt ut labore et dolore magna aliquyam erat, sed diam voluptua. At vero eos et accusam et justo duo dolores et ea rebum. Stet clita kasd gubergren, no sea takimata sanctus est</p>
  </div>
  <div class="product-photo" style="left:228px;top:45px;width:105px;height:88px" role="img" aria-label="Produktfoto: Ringordner mit Register"></div>
  <div class="product-photo" style="left:28px;top:190px;width:110px;height:100px" role="img" aria-label="Produktfoto: Schuber mit Ordner"></div>
  <div class="item" style="left:160px;top:190px;width:173px">
    <h2>Schuber</h2>
    <p>Lorem ipsum dolor sit amet, consetetur sadipscing elitr, sed diam nonumy eirmod tempor invidunt ut labore et dolore magna aliquyam erat, sed diam voluptua. At vero eos et accusam et justo duo dolores et ea rebum. Stet clita kasd gubergren, no sea takimata sanctus est</p>
  </div>
  <div class="item" style="left:28px;top:330px;width:185px">
    <h2>Schreibmappen</h2>
    <p>Lorem ipsum dolor sit amet, consetetur sadipscing elitr, sed diam nonumy eirmod tempor invidunt ut labore et dolore magna aliquyam erat, sed diam voluptua. At vero eos et accusam et justo duo dolores et ea rebum. Stet clita kasd gubergren, no sea takimata sanctus est</p>
  </div>
  <div class="product-photo" style="left:228px;top:312px;width:105px;height:90px" role="img" aria-label="Produktfoto: Schreibmappe mit Stift"></div>
  <span class="accent br"></span>
</section>

</body>
</html>
```